Shipping and Logistics, Project

Project description : Company Profile

A total logistics company covering domestic / international freight forwarding, warehouse management services, haulage, supply chain management, transport management & distribution, procurement & assembly services, shipping, chartering & bunker services, project logistics & tax exemption consultancy, oil & gas logistics, halal logistics services & integrated logistics management. We’re a well-established and experienced freight forwarder in Kuala Lumpur, Malaysia. We specialize in customized value-added solution that optimizes your supply chain by trimming inventory, reducing logistics cost and enhancing your customer service levels.

As a member of the Continental Parcel and Carriage Alliance which comprise of 170 global freight agents in 80 countries that promotes great handling in cross-trade logistics and freighting. You could rely on our efficiency in handlings of export cargo (FCL, LCL, Bulk and Conventional) between our global network offices worldwide with a total scale of 10,000 groomed specialists in various logistics division working together to ensure delivery task meets with your expectation. With our dedicated qualified and experienced professionals, we are fully committed to serving our clients.

Our generic services are listed below for your reference:

• Air Freight
• Ocean Freight FCL & LCL
• Container Haulage
• Warehousing
• Transportation and Distribution within Malaysia and Thailand
• Cross-Border Road Line-hauls between Thailand, Malaysia, Singapore and Laos
• Customs Brokerage and Forwarding
• Project Cargo Freight Forwarding for setting up of new plants / factories and ad hoc heavy-lift
• Air-Sea-Road-Rail multi-modal options
• Import / Export / Storage / Documentation / Handling of DG / Hazmat
• Vessel and Aircraft Charters

Our Mission
Based on the motto “Quick, Reliable and Polite”, we are dedicated to upholding the following three points corporate philosophy:
1. Adhering to the principle that “the customer always comes first”.
2. Contributing to the development of the local community.
3. Making it our duty to be responsible and sincere.

Our Edge
• One-Stop Logistics Solutions
• Extensive Network Throughout Malaysia
• Highly Qualified and Experienced Pool of Professionals
• Comprehensive IT Solutions
• Innovative and Customer-focused Solutions
• Flexible and Consistent in Managing Exceptions
• Total Supply Chain Visibility

Target Market
1. We sell the logistics services to all the industry in Malaysia and Worldwide. (ONE Stop Logistics Solutions)

Competitor
1. RT Vollmark
2. Corventa Transport
3. Brastow + Feld
4. TOLRI
5. QVN
6. Trundelles
7. Wiro Logistics

Rules for Picking a Company Name
1. Unique and unforgettable
2. Avoid unusual spellings
3. Easy to pronounce and remember
4. Keep it simple
5. Make some sense
6. Give a clue

Rules for Picking a Company Logo
4. Keep it simple
5. Make some sense
6. Give a clue

1. Simplicity
2. Memorability
3. Originality
4. Modern Yet Timeless
5. Balance
6. Complementary
7. Versatility

Stationery Information
1. Company Name : Tenhaul Solutions Sdn Bhd
2. Company Registration : 2738516-P
3. Address : 42-07, Jalan Seri Dedap 5, Taman Bukit Kenari, 81100 Johor Bahru, Johor, Malaysia.
4. Name : Derek Tan
5. Position : Manager
6. Mobile No : (+6019) 4183907
7. Office No : (+607) 2918476
8. Fax No : Not Available
9. Email Address : derek.tan@tenhaul-solutions.example
10. Web Domain : www.tenhaul-solutions.example
11. Company Slogan : Freight Without Borders

Target Market(s)

Corporate Company

Industry/Entity Type

Shipping and Logistics Industry

Requirements
Must have
• Company Full Name : TENHAUL SOLUTIONS SDN. BHD.
Nice to have
• Keep it simple and unforgettable ...

```html
<!DOCTYPE html>
<html lang="en">
<head>
<meta charset="utf-8">
<title>Tenhaul Solutions – Business Card</title>
<link href="https://fonts.googleapis.com/css2?family=Montserrat:wght@400;500;700&display=swap" rel="stylesheet">
<style>
  :root {
    --bg: #d6d6d6;
    --blue: #2f86dc;
    --ink: #222222;
    --paper: #ffffff;
    --dark: #272727;
    --light-text: #ffffff;
  }
  * { box-sizing: border-box; margin: 0; padding: 0; }
  html, body { width: 1200px; height: 913px; overflow: hidden; }
  body {
    background: var(--bg);
    font-family: "Montserrat", sans-serif;
    color: var(--ink);
    position: relative;
  }
  .card {
    position: absolute;
    width: 520px;
    height: 300px;
    box-shadow: 0 14px 30px rgba(0,0,0,0.25);
  }
  /* Front */
  .card-front {
    left: 70px; top: 150px;
    background: var(--paper);
    border: 2px solid var(--blue);
  }
  .brand { display: flex; align-items: center; gap: 10px; }
  .brand-mark { width: 22px; height: 22px; background: var(--blue); flex: none; }
  .brand-name { font-weight: 700; letter-spacing: 1px; color: var(--blue); white-space: nowrap; }
  .card-front .brand { position: absolute; right: 26px; top: 26px; }
  .card-front .brand-name { font-size: 22px; }
  .address {
    position: absolute; right: 26px; top: 82px;
    width: 250px;
    border-top: 1px solid var(--ink);
    padding-top: 8px;
    text-align: right;
    font-size: 11.5px; line-height: 1.5;
  }
  .person { position: absolute; left: 26px; top: 112px; width: 250px; }
  .person-name { font-size: 22px; font-weight: 700; color: var(--blue); }
  .person-role { font-size: 12px; margin-top: 2px; padding-bottom: 8px; border-bottom: 1px solid var(--ink); }
  .contacts { list-style: none; margin-top: 8px; font-size: 11.5px; line-height: 1.6; }
  .contacts li { display: flex; align-items: center; gap: 8px; white-space: nowrap; }
  .contacts svg { width: 11px; height: 11px; flex: none; }
  .reg-band {
    position: absolute; left: 0; right: 0; bottom: 0; height: 34px;
    background: var(--blue); color: var(--light-text);
    font-size: 13px; display: flex; align-items: center; justify-content: flex-end;
    padding-right: 26px;
  }
  /* Back */
  .card-back {
    left: 630px; top: 463px;
    background: var(--dark);
    border: 2px solid var(--blue);
    display: flex; flex-direction: column; align-items: center; justify-content: center; gap: 38px;
  }
  .card-back .brand-mark { width: 34px; height: 34px; }
  .card-back .brand-name { font-size: 32px; color: var(--light-text); letter-spacing: 2px; }
  .slogan { font-size: 20px; font-weight: 700; color: var(--light-text); }
</style>
</head>
<body>
  <section class="card card-front">
    <div class="brand">
      <span class="brand-mark"></span>
      <span class="brand-name">TENHAUL SOLUTIONS</span>
    </div>
    <p class="address">Tenhaul Solutions Sdn Bhd<br>42-07, Jalan Seri Dedap 5,<br>Taman Bukit Kenari, 81100<br>Johor Bahru, Johor, Malaysia.</p>
    <div class="person">
      <h1 class="person-name">Derek Tan</h1>
      <p class="person-role">Manager</p>
      <ul class="contacts">
        <li><svg viewBox="0 0 12 12"><rect x="3" y="0.5" width="6" height="11" rx="1" fill="none" stroke="#2f86dc" stroke-width="1.4"/></svg>(+6019) 4183907</li>
        <li><svg viewBox="0 0 12 12"><path d="M1 4 Q6 0 11 4 L9 5 L8 3.5 Q6 3 4 3.5 L3 5 Z M2 6 H10 V11 H2 Z" fill="#2f86dc"/></svg>(+607) 2918476</li>
        <li><svg viewBox="0 0 12 12"><rect x="0.5" y="2" width="11" height="8" fill="#2f86dc"/><path d="M0.5 2 L6 6.5 L11.5 2" fill="none" stroke="#fff" stroke-width="1"/></svg>derek.tan@tenhaul-solutions.example</li>
        <li><svg viewBox="0 0 12 12"><circle cx="6" cy="6" r="5.5" fill="#2f86dc"/><path d="M0.5 6 H11.5 M6 0.5 V11.5" stroke="#fff" stroke-width="0.8"/></svg>www.tenhaul-solutions.example</li>
      </ul>
    </div>
    <div class="reg-band">Company Registration : 2738516-P</div>
  </section>

  <section class="card card-back">
    <div class="brand">
      <span class="brand-mark"></span>
      <span class="brand-name">TENHAUL SOLUTIONS</span>
    </div>
    <p class="slogan">Freight Without Borders</p>
  </section>
</body>
</html>
```